BUSINESS CARD DESIGN

NAME- TODD MARSHECK
PHONE NUMER - 808- 555-0147
EMAIL- OFFICE@VORN-GRADEWORKS.COM
BACK OF CARD- SPEACIALIZES IN LAND CLEARING, FORESTRY MUCLHING AND EXCAVATION

Contact Information for Business Card

NAME- TODD MARSHECK PHONE NUMER - 808- 555-0147 EMAIL- OFFICE@VORN-GRADEWORKS.COM BACK OF CARD- SPEACIALIZES IN LAND CLEARING , MUCLHING AND EXCAVATION

```html
<!DOCTYPE html>
<html lang="en">
<head>
<meta charset="utf-8">
<title>Todd Marsheck — Business Card</title>
<link href="https://fonts.googleapis.com/css2?family=Montserrat:wght@400;500;700&display=swap" rel="stylesheet">
<style>
  :root {
    --backdrop: #1b1b1b;
    --card-light: #f7f7f7;
    --card-dark: #2b2b2b;
    --ink: #262626;
    --ink-soft: #333333;
    --paper-text: #ffffff;
  }
  html, body {
    margin: 0;
    padding: 0;
    width: 1200px;
    height: 1059px;
    overflow: hidden;
    background: var(--backdrop);
    font-family: "Montserrat", sans-serif;
  }
  .stage {
    position: relative;
    width: 1200px;
    height: 1059px;
  }
  .card {
    position: absolute;
    box-sizing: border-box;
    text-align: center;
  }
  .card--front {
    left: 256px;
    top: 89px;
    width: 688px;
    height: 390px;
    background: var(--card-light);
    color: var(--ink);
  }
  .card--back {
    left: 254px;
    top: 547px;
    width: 693px;
    height: 393px;
    background: var(--card-dark);
    color: var(--paper-text);
  }
  .name {
    position: absolute;
    left: 0; right: 0;
    top: 68px;
    margin: 0;
    font-weight: 700;
    font-size: 39px;
    letter-spacing: 1.5px;
  }
  .title {
    position: absolute;
    left: 0; right: 0;
    top: 118px;
    margin: 0;
    font-weight: 400;
    font-size: 23px;
    letter-spacing: 1.5px;
    color: var(--ink-soft);
  }
  .icons {
    position: absolute;
    left: 0; right: 0;
    top: 163px;
    display: flex;
    justify-content: center;
    gap: 4px;
  }
  .icons svg { width: 24px; height: 24px; }
  .contact {
    position: absolute;
    left: 0; right: 0;
    top: 209px;
    margin: 0;
    padding: 0;
    list-style: none;
    font-size: 22px;
    letter-spacing: 1.5px;
    color: var(--ink-soft);
  }
  .contact li { height: 41px; line-height: 28px; }
  .specialty {
    position: absolute;
    left: 0; right: 0;
    top: 150px;
    margin: 0;
    font-weight: 500;
    font-size: 27px;
    line-height: 47px;
    letter-spacing: 1.4px;
  }
</style>
</head>
<body>
<main class="stage">
  <section class="card card--front">
    <h1 class="name">TODD MARSHECK</h1>
    <p class="title">DIRECTOR</p>
    <div class="icons" aria-hidden="true">
      <svg viewBox="0 0 24 24" class="icon icon--phone">
        <circle cx="12" cy="12" r="12" fill="#262626"/>
        <path d="M6.5 10.5c0-2 2.5-3 5.5-3s5.5 1 5.5 3v1h-2.5v-1.5h-6v1.5H6.5z" fill="#fff"/>
        <rect x="8" y="11.5" width="8" height="5" rx="1" fill="#fff"/>
      </svg>
      <svg viewBox="0 0 24 24" class="icon icon--mail">
        <circle cx="12" cy="12" r="12" fill="#262626"/>
        <rect x="6" y="8" width="12" height="8.5" fill="#fff"/>
        <path d="M6 8l6 5 6-5" fill="none" stroke="#262626" stroke-width="1.2"/>
      </svg>
      <svg viewBox="0 0 24 24" class="icon icon--globe">
        <circle cx="12" cy="12" r="12" fill="#262626"/>
        <circle cx="12" cy="12" r="6" fill="#fff"/>
        <path d="M9 8.5c1.5.5 1 2 2.5 2.5s.5 2 2 2.5M14 7.5c-.5 1 .5 1.5 1.5 1.8M10 16c.3-1 1.5-1.3 2.5-1" fill="none" stroke="#262626" stroke-width="1.3"/>
      </svg>
    </div>
    <ul class="contact">
      <li class="contact__phone">808- 555-0147</li>
      <li class="contact__email">OFFICE@VORN-GRADEWORKS.COM</li>
      <li class="contact__web">WWW.VORN-GRADEWORKS.COM</li>
    </ul>
  </section>

  <section class="card card--back">
    <p class="specialty">SPEACIALIZES IN LAND CLEARING<br>MUCLHING AND EXCAVATION</p>
  </section>
</main>
</body>
</html>
```